Luxury Face Oil Label

I'm looking for a simple and sophisticated design for a natural face oil that will target the luxe market. It is a pure Natural product. I have attached the logo, Velmora Organics.

Here's the Copy

SERA FACIAL OIL

Regenerate. Hydrate. Glow

100% Natural

30ml (1.01 oz)

A complex blend of Pure Oils including Marula, Sea Buckthorn, Rosehip, Neroli, Evening primrose, Argan, Calendula, Lavender, Jojoba, Grapeseed, Baobab, Moringa and Vitamin E oil.

Produced by
Copper Lantern Ltd
P.O box 7825-00300
Nairobi, Kenya
www.velmoraorganics.example

Target Market(s)

High end

Requirements
Must have
• Simple, Please consider the bottle, which is a 30ml clear glass bottle with a gold and white pump. Image attached.
Nice to have
• Very clean designs, not too much going on.
Should not have
• Leaves and nuts.

```html
<!DOCTYPE html>
<html lang="en">
<head>
<meta charset="utf-8">
<title>Velmora Organics – Sera Facial Oil Labels</title>
<link href="https://fonts.googleapis.com/css2?family=Raleway:wght@300;400;500;700&display=swap" rel="stylesheet">
<style>
  :root {
    --ink: #4b4e46;
    --ink-soft: #5e6159;
    --rule: #9a9c96;
    --edge: #b9bab6;
    --paper: #ffffff;
    --stage: #ffffff;
  }
  * { box-sizing: border-box; margin: 0; padding: 0; }
  html, body {
    width: 1200px; height: 848px; overflow: hidden;
    background: var(--stage);
    font-family: "Raleway", sans-serif;
    color: var(--ink);
  }
  .sheet { position: relative; width: 1200px; height: 848px; }
  .label {
    position: absolute; top: 153px;
    width: 330px; height: 542px;
    background: var(--paper);
    border: 1px solid var(--edge);
    border-radius: 7px;
    display: flex; flex-direction: column; align-items: center;
    text-align: center;
  }
  .label--front { left: 200px; }
  .label--back { left: 670px; }

  /* Front */
  .brand {
    margin-top: 27px;
    width: 206px; height: 206px;
    display: flex; align-items: center; justify-content: center;
  }
  .brand__name {
    font-weight: 400; font-size: 24px; letter-spacing: 6px;
    line-height: 1.5; text-transform: uppercase; color: var(--ink);
  }
  .product-name {
    margin-top: 40px;
    font-weight: 700; font-size: 50px; line-height: 1; letter-spacing: 1px;
  }
  .product-type {
    margin-top: 12px;
    font-weight: 400; font-size: 25px; letter-spacing: 7px;
    color: var(--ink-soft);
  }
  .benefits {
    margin-top: 32px;
    font-weight: 400; font-size: 20px; color: var(--ink-soft);
  }
  .claim {
    margin-top: 8px;
    font-weight: 500; font-size: 20px;
  }
  .volume {
    margin-top: 12px;
    font-weight: 400; font-size: 19px; color: var(--ink-soft);
  }

  /* Back */
  .rule { width: 128px; height: 1px; background: var(--rule); }
  .rule--top { margin-top: 29px; }
  .ingredients {
    margin-top: 12px; width: 212px;
    font-weight: 300; font-size: 20.5px; line-height: 26.8px;
  }
  .rule--mid { margin-top: 12px; }
  .producer {
    margin-top: 12px;
    font-weight: 400; font-size: 20px; line-height: 26.8px;
  }
  .producer__company { font-weight: 500; }
  .website {
    margin-top: 10px;
    font-weight: 400; font-size: 19.5px;
  }
</style>
</head>
<body>
<main class="sheet">
  <section class="label label--front" aria-label="Front label">
    <div class="brand">
      <p class="brand__name">Velmora<br>Organics</p>
    </div>
    <h1 class="product-name">SERA</h1>
    <p class="product-type">FACIAL OIL</p>
    <p class="benefits">Regenerate | Hydrate | Glow</p>
    <p class="claim">100% Natural</p>
    <p class="volume">30ml (1.01 oz)</p>
  </section>

  <section class="label label--back" aria-label="Back label">
    <div class="rule rule--top"></div>
    <p class="ingredients">A complex blend of pure oils including marula, sea buckthorn, rosehip, neroli, evening primrose, argan, calendula, lavender, jojoba, grapeseed, baobab, moringa and vitamin e oil.</p>
    <div class="rule rule--mid"></div>
    <p class="producer">
      Produced by<br>
      <span class="producer__company">Copper Lantern Ltd</span><br>
      P.O Box 7825-00300<br>
      Nairobi, Kenya
    </p>
    <p class="website">www.velmoraorganics.example</p>
  </section>
</main>
</body>
</html>
```